Gourmet cookie company needs a label designed

We need a label designed for a new cookie company. We make mini cookies. The labels will be placed on either white tins or clear containers. We would like some bright and eye catching label although not child like. Our target customer is adults not kids.
Any color/colors acceptable. The initial label will be a square 4" label but the design should also be able to be formatted to fit on a round label as well in the future.

Text on label: Rosalind's Wafer Crumb Company; Chocolate Chip; All Natural; New Wt. 8.0oz

```html
<!DOCTYPE html>
<html lang="en">
<head>
<meta charset="utf-8">
<title>Rosalind's Wafer Crumb Company – Chocolate Chip Label</title>
<link rel="stylesheet" href="https://fonts.googleapis.com/css2?family=Jost:wght@400;500&family=Fira+Sans+Condensed:wght@800&display=swap">
<style>
  :root {
    --page: #ffffff;
    --frame-grey: #8a8a8a;
    --label-blue: #0a7cc4;
    --label-blue-deep: #0a82c8;
    --label-blue-light: #d9ecfa;
    --rule-white: #ffffff;
    --brand-yellow: #f3ef3b;
    --ribbon-brown: #9c6b3c;
    --ink-dark: #111111;
    --shadow: rgba(0, 40, 90, 0.45);
  }
  html, body {
    margin: 0;
    width: 1200px;
    height: 900px;
    overflow: hidden;
    background: var(--page);
  }
  .canvas {
    position: relative;
    width: 1200px;
    height: 900px;
  }
  .label-art {
    position: absolute;
    inset: 0;
    width: 1200px;
    height: 900px;
  }
  .brand-name {
    font-family: "Jost", sans-serif;
    font-weight: 500;
    fill: var(--brand-yellow);
  }
  .flavour-name {
    font-family: "Fira Sans Condensed", sans-serif;
    font-weight: 800;
    font-size: 54px;
    fill: var(--ink-dark);
  }
  .claim {
    font-family: "Jost", sans-serif;
    font-weight: 400;
    fill: var(--rule-white);
  }
</style>
</head>
<body>
<main class="canvas">
  <svg class="label-art" viewBox="0 0 1200 900" xmlns="http://www.w3.org/2000/svg">
    <defs>
      <radialGradient id="label-glow" cx="600" cy="430" r="560" gradientUnits="userSpaceOnUse">
        <stop offset="0" stop-color="var(--label-blue-light)"/>
        <stop offset="0.45" stop-color="#62a9df"/>
        <stop offset="1" stop-color="var(--label-blue)"/>
      </radialGradient>
      <filter id="ribbon-shadow" x="-10%" y="-20%" width="130%" height="150%">
        <feDropShadow dx="8" dy="10" stdDeviation="5" flood-color="var(--shadow)"/>
      </filter>
    </defs>

    <rect class="trim-frame" x="179.5" y="28.5" width="842" height="843" fill="none" stroke="var(--frame-grey)" stroke-width="1"/>

    <rect class="label-body" x="207" y="57" width="786" height="786" fill="url(#label-glow)"/>

    <path class="lower-band-edge" d="M 207 628 C 300 680, 420 695, 600 665 S 880 618, 993 625 L 993 843 L 207 843 Z" fill="var(--rule-white)"/>
    <path class="lower-band" d="M 207 640 C 300 692, 420 707, 600 677 S 880 630, 993 637 L 993 843 L 207 843 Z" fill="var(--label-blue-deep)"/>

    <rect class="inner-keyline" x="216" y="66" width="768" height="768" fill="none" stroke="var(--rule-white)" stroke-width="3"/>

    <text class="brand-name" x="600" y="250" text-anchor="middle" font-size="78">Rosalind's</text>
    <text class="brand-name" x="600" y="320" text-anchor="middle" font-size="40">Wafer Crumb Company</text>

    <g class="flavour-ribbon" filter="url(#ribbon-shadow)">
      <path d="M 343 460 C 450 430, 560 460, 650 470 S 800 455, 858 428 L 858 538 C 800 560, 720 565, 640 560 S 450 520, 343 580 Z" fill="var(--rule-white)"/>
      <path d="M 352 467 C 455 438, 560 468, 650 478 S 795 465, 849 441 L 849 532 C 795 552, 720 557, 640 552 S 450 512, 352 568 Z" fill="var(--ribbon-brown)"/>
    </g>
    <text class="flavour-name" x="600" y="524" text-anchor="middle">CHOCOLATE CHIP</text>

    <text class="claim" x="600" y="743" text-anchor="middle" font-size="36">All Natural</text>
    <text class="claim" x="600" y="808" text-anchor="middle" font-size="30">New Wt. 8.0oz</text>
  </svg>
</main>
</body>
</html>
```